Billboard Design

Billboard design featuring the colors dark teal and dark grey.
Company: Cedarbrook Hollow Properties
Services Real Estate & Management
Phone: 614-739-5081
Important info:
Professionalizing Property Management
Specialized training and credentials in Property Management
Serving single family, multifamily, complexes, and mixed use properties.

UPDATE: We have uploaded photos from a recent project of ours and would love to see them used on the billboard.

```html
<!DOCTYPE html>
<html lang="en">
<head>
<meta charset="utf-8">
<title>Cedarbrook Hollow Properties Billboard</title>
<link rel="stylesheet" href="https://fonts.googleapis.com/css2?family=Poppins:wght@400;500;600;700;800&display=swap">
<style>
  :root {
    --teal: #0b7f7d;
    --charcoal: #2d2a2a;
    --ink: #222222;
    --paper: #ffffff;
  }
  * { margin: 0; padding: 0; box-sizing: border-box; }
  html, body { width: 1200px; height: 475px; overflow: hidden; background: var(--paper); }
  .billboard {
    position: relative;
    width: 1200px;
    height: 475px;
    overflow: hidden;
    font-family: "Poppins", sans-serif;
    background: linear-gradient(135deg, var(--paper) 0%, #f4f4f4 45%, var(--paper) 100%);
  }
  .backdrop { position: absolute; inset: 0; }
  .brand {
    position: absolute; left: 15px; top: 20px; width: 166px; height: 74px;
    border: 2px solid var(--ink); background: var(--paper);
    display: flex; align-items: center; justify-content: center; gap: 8px;
  }
  .brand-mark { width: 14px; height: 14px; background: var(--teal); }
  .brand-name { font-size: 13px; font-weight: 600; color: var(--ink); line-height: 1.15; }
  .headline {
    position: absolute; left: 13px; top: 108px;
    color: var(--teal); font-weight: 700; line-height: 52px; letter-spacing: -0.3px;
    white-space: nowrap;
  }
  .headline span { display: block; }
  .headline .first { font-size: 44.5px; }
  .headline .second { font-size: 41.5px; }
  .tagline {
    position: absolute; left: 14px; top: 220px;
    color: var(--ink); font-size: 17px; font-weight: 500; white-space: nowrap;
  }
  .coverage {
    position: absolute; left: 14px; top: 253px;
    color: var(--ink); font-size: 14.5px; font-weight: 400; white-space: nowrap;
  }
  .services-label {
    position: absolute; left: 14px; top: 312px; width: 172px; height: 50px;
    background: var(--charcoal); color: var(--paper);
    font-weight: 700; font-size: 30px; line-height: 50px; padding-left: 6px;
  }
  .service {
    position: absolute; top: 300px; width: 72px; height: 72px; border-radius: 50%;
    background: var(--teal); border: 3px solid var(--paper);
    box-shadow: 0 0 0 1.5px var(--teal);
    color: var(--paper); text-align: center;
    display: flex; flex-direction: column; align-items: center; justify-content: center; gap: 1px;
  }
  .service svg { width: 30px; height: 30px; }
  .service-name { font-size: 7px; font-weight: 500; }
  .service.real-estate { left: 186px; }
  .service.management { left: 260px; }
  .call { position: absolute; left: 15px; top: 396px; display: flex; gap: 5px; }
  .call svg { width: 22px; height: 64px; margin-top: 2px; }
  .call-label { color: var(--ink); font-size: 20px; line-height: 22px; font-weight: 400; }
  .call-number { color: var(--teal); font-size: 39px; line-height: 44px; font-weight: 700; letter-spacing: -0.5px; white-space: nowrap; }
  .follow { position: absolute; left: 476px; top: 396px; width: 104px; text-align: center; }
  .follow-label { color: var(--teal); font-size: 12.5px; font-weight: 400; white-space: nowrap; }
  .social { display: flex; justify-content: center; gap: 5px; margin-top: 6px; }
  .social span { width: 30px; height: 30px; border-radius: 50%; background: var(--charcoal); }
</style>
</head>
<body>
<div class="billboard">
  <svg class="backdrop" width="1200" height="475" viewBox="0 0 1200 475">
    <defs>
      <linearGradient id="scene-tones" x1="0" y1="0" x2="0" y2="1">
        <stop offset="0" stop-color="#c9d6de"/>
        <stop offset="0.25" stop-color="#8a9a78"/>
        <stop offset="0.45" stop-color="#b39c86"/>
        <stop offset="0.8" stop-color="#a8927e"/>
        <stop offset="1" stop-color="#7f9a5c"/>
      </linearGradient>
    </defs>
    <polygon points="626,0 1200,0 1200,475 748,475" fill="url(#scene-tones)" role="img" aria-label="Photo of a brick two-storey family home with a smiling family holding house keys in front"/>
    <polygon points="562,0 616,0 741,475 686,475" fill="var(--teal)"/>
    <polygon points="616,0 626,0 748,475 741,475" fill="var(--paper)"/>
    <polygon points="682,253 741,475 586,475" fill="var(--charcoal)"/>
  </svg>

  <div class="brand">
    <span class="brand-mark"></span>
    <span class="brand-name">Cedarbrook Hollow<br>Properties</span>
  </div>

  <h1 class="headline">
    <span class="first">PROFESSIONALIZING</span>
    <span class="second">PROPERTY MANAGEMENT</span>
  </h1>
  <p class="tagline">Specialized training and credentials in Property Management</p>
  <p class="coverage">Serving single family, multifamily, complexes, and mixed use properties.</p>

  <div class="services-label">SERVICES:</div>
  <div class="service real-estate">
    <svg viewBox="0 0 24 24"><path d="M12 3 2 12h3v8h5v-5h4v5h5v-8h3z" fill="#fff"/></svg>
    <span class="service-name">REAL ESTATE</span>
  </div>
  <div class="service management">
    <svg viewBox="0 0 24 24"><circle cx="10" cy="7" r="4" fill="#fff"/><path d="M3 21c0-5 3-8 7-8s7 3 7 8z" fill="#fff"/><circle cx="18" cy="16" r="3" fill="none" stroke="#fff" stroke-width="2"/></svg>
    <span class="service-name">MANAGEMENT</span>
  </div>

  <div class="call">
    <svg viewBox="0 0 22 64"><rect x="1.5" y="1.5" width="19" height="61" rx="3" fill="none" stroke="var(--teal)" stroke-width="3"/><rect x="8" y="57" width="6" height="2" fill="var(--teal)"/></svg>
    <div>
      <p class="call-label">CALL US ON</p>
      <p class="call-number">614-739-5081</p>
    </div>
  </div>

  <div class="follow">
    <p class="follow-label">FOLLOW US ON</p>
    <div class="social"><span></span><span></span><span></span></div>
  </div>
</div>
</body>
</html>
```